Vermilion Reel Works Web Design

COMPANY: VERMILION REEL WORKS
LOCATION: SHANGHAI, CHINA
AREA: FILM/TV DRAMA/COMMERCIALS/GAME POST PRODUCTION, SOUND DESIGN, MUSIC, and GAME.
WEB STYLE: SIMPLE, PROFESSIONAL, TRUSTWORTHY

LANGUAGE: ENGLISH, CHINESE. (Same layout, different language)
UPDATE: AFTER PROJECT FINISHED, WE NEED UPDATE BY OURSELVES.

MAIN SUBJECT: 6
1 HOMEPAGE
2 ABOUT US
3 TEAM
4 SERVICES
5 FACILITY
6 CONTACT

add one page of JOB OPPORTUNITIES.

DETAILS
1 HOMEPAGE
SLOGAN: Vermilion Reel Works provides a well-designed working environment which amplifies your team’s ability to reach their creative goals.

Our services include:
 Feature Films
 Music & Scoring
 Commercials
 ADR & Foley
 Sound & Picture Editorial
 Sound Design
 Video Game

2 ABOUT US
Vermilion Reel Works is located in the premiere South-Bund area of Shanghai. Occupying a 5000 square meter Technical Building, Vermilion Reel Works was built by a filmmaker for filmmakers, and is one of the largest, most versatile full-service post-production facilities in China.

Vermilion Reel Works is positioning to be at the forefront of the latest technology. Our goal is to provide a comprehensive solution for the post-production needs of our clients. We offer two fully-equipped dubbing stages (one of which will be certified KESTRON VOXAR PREMIERE), a large variety of both picture and sound editing rooms, impressive Foley and ADR stages, a world-class scoring stage, and complete audio and video transfer services.

We can handle your entire project from editing all the way to the end of the final sound mix; all under one extremely comfortable roof. We fully realize that the true art is in listening to the needs of our clients and making their greatest vision a reality. To this end our creative team's expertise, with a network of sound supervisors, editors and mixers, will deliver the magic you need. Producers and directors will also find our richly appointed guest accommodations to be a comfortable and soothing place to wind up the day. Every aspect of your project will be taken care of by a skilled and dedicated team, in the way that is best suited to you.

3 TEAM
(attachment 01)

4 SERVICES
Sound Mix
ADR
FOLEY
MUSIC
Sound Design
Sound Edit
Picture Edit
for all the Films, TV Drama, Commercials, Video Games, Online Media
(attachment 02, use photo)

5 FACILITY
(attachment 03)

6 CONTACT
(attachment04)
with map

Project Deadline Extended
Reason: Designers work are great, my bosses will spend 1-2 days select one of these web design, and spend 1-2 days to make some change, maybe use new photos.

```html
<!DOCTYPE html>
<html lang="en">
<head>
<meta charset="utf-8">
<title>Vermilion Reel Works</title>
<link href="https://fonts.googleapis.com/css2?family=Roboto:wght@400;500;700&family=Oxygen:wght@400;700&family=Noto+Serif:wght@700&display=swap" rel="stylesheet">
<style>
:root{
  --navy:#2a3f73;
  --ink:#333;
  --grey-band:#ececec;
  --rule:#d6d6d6;
  --white:#fff;
}
*{margin:0;padding:0;box-sizing:border-box}
html,body{width:974px;height:1200px;overflow:hidden;background:var(--white)}
body{position:relative;font-family:"Oxygen",sans-serif;color:var(--ink)}
.abs{position:absolute}

/* header */
.site-header{left:0;top:0;width:974px;height:101px;background:linear-gradient(#fff,#f1f1f1);border-bottom:1px solid #ddd}
.brand{left:115px;top:22px;width:122px;text-align:center;border-bottom:2px solid #9aa;padding-bottom:6px}
.brand-name{font-family:"Roboto",sans-serif;font-weight:700;font-size:20px;color:var(--navy);letter-spacing:.5px;display:block}
.brand-sub{font-family:"Roboto",sans-serif;font-weight:700;font-size:10px;color:var(--navy);letter-spacing:.3px;display:block;margin-top:2px}
.call{left:558px;top:13px;display:flex;gap:8px;align-items:flex-start}
.call-label{font-family:"Roboto",sans-serif;font-size:12px;color:#444}
.call-number{font-family:"Roboto",sans-serif;font-weight:700;font-size:16px;color:var(--navy);margin-top:1px}
.lang{left:728px;top:18px;width:133px;height:28px;border:2px solid #ccc;background:#f8f8f8;font-family:"Roboto",sans-serif;font-size:12px;color:#444;padding:5px 0 0 14px}
.lang svg{position:absolute;right:10px;top:9px}
.nav{left:300px;top:74px;display:flex;font-family:"Roboto",sans-serif;font-weight:500;font-size:12.5px;color:#444}
.nav a{color:inherit;text-decoration:none;padding:0 10px;border-left:1px solid #999;line-height:15px}
.nav a:first-child{border-left:none;color:var(--navy);padding-right:18px}

/* hero */
.hero{left:0;top:101px;width:974px;height:361px;background:linear-gradient(100deg,#3a2a1c 0%,#7a5a38 30%,#b5824c 55%,#6a4a2e 80%,#c58b4e 100%)}
.hero-caption{left:0;top:399px;width:974px;height:63px;background:rgba(20,14,10,.72);border-bottom:3px solid #222;color:#fff;font-family:"Noto Serif",serif;font-weight:700;font-size:18px;line-height:27px;text-align:center;padding-top:6px}
.hero-arrow{width:29px;height:29px;border-radius:50%;background:#111;top:233px}

/* section titles */
.section-title{left:0;width:974px;display:flex;justify-content:center;align-items:center;gap:12px;font-family:"Roboto",sans-serif;font-weight:500;font-size:21px;color:#333;line-height:26px;white-space:nowrap}
.title-rule{flex:none;display:block}
.title-rule.right{transform:scaleX(-1)}

/* about */
.about-text{left:120px;top:512px;width:734px;text-align:center;font-size:10.5px;line-height:16px;color:#444}
.about-text p+p{margin-top:4px}
.read-more{left:0;width:974px;top:587px;text-align:center;font-family:"Roboto",sans-serif;font-weight:500;font-size:12px;color:#222}

/* services */
.services{left:0;top:607px;width:974px;height:217px;background:var(--grey-band);border-top:1px solid #ddd;border-bottom:1px solid #ddd}
.service{width:140px;text-align:center;top:672px}
.service-disc{width:92px;height:92px;border-radius:50%;margin:0 auto;background:radial-gradient(circle at 50% 40%,#eee,#cfcfcf);box-shadow:0 2px 4px rgba(0,0,0,.2);display:flex;align-items:center;justify-content:center}
.service-label{font-family:"Roboto",sans-serif;font-weight:500;font-size:12.5px;color:#333;margin-top:21px}
.svc-arrow{width:28px;height:28px;border-radius:50%;background:#c8c8c8;top:704px}

/* columns */
.col-title{font-family:"Roboto",sans-serif;font-weight:700;font-size:17px;color:#333;display:flex;align-items:center;gap:8px;border-bottom:1px solid var(--rule);padding-bottom:4px;white-space:nowrap}
.col-title em{font-style:normal;color:var(--navy)}
.facility-list{list-style:none;font-size:9.8px;line-height:22px;color:#333;white-space:nowrap}
.facility-list li::before{content:"•";margin-right:7px}
.link-more{font-family:"Roboto",sans-serif;font-weight:500;font-size:12px;color:var(--navy)}
.quote{left:372px;top:895px;width:228px;height:106px;background:#ebebeb;border-radius:6px;font-style:italic;font-size:9.4px;line-height:16px;color:#444;padding:10px 6px 0 16px;letter-spacing:-.1px}
.avatar{left:388px;top:983px;width:54px;height:55px;background:linear-gradient(#f1f1f1,#8a8f99);border:1px solid #ccc;border-radius:3px}
.field{left:632px;width:228px;height:23px;border:1px solid #bbb;border-radius:3px;background:#fff;font-style:italic;font-size:10px;color:#666;padding:4px 8px}
.submit{left:630px;top:1024px;width:55px;height:19px;background:var(--navy);color:#fff;border-radius:2px;font-family:"Roboto",sans-serif;font-weight:700;font-size:11.5px;text-align:center;line-height:19px}

/* footer */
.site-footer{left:0;top:1075px;width:974px;height:125px;background:var(--navy);border-top:2px solid #ccc}
.foot-box{top:1091px;height:62px;border:1px solid #5a6d98;background:#354a7c;color:#fff;padding:8px 10px}
.foot-box h4{font-family:"Oxygen",sans-serif;font-size:11.5px;font-weight:700;margin-bottom:7px}
.foot-contact{font-size:9px;line-height:16px;display:flex;align-items:center;gap:8px;white-space:nowrap}
.email-input{width:146px;height:22px;background:#5d6f97;font-style:italic;font-size:9.5px;padding:5px 8px;color:#e6e9f0}
.go{width:25px;height:22px;background:#5d6f97;margin-left:7px;display:flex;align-items:center;justify-content:center}
.social{width:19px;height:19px;border-radius:3px}
.foot-nav{left:115px;top:1173px;display:flex;font-size:11px;color:#fff}
.foot-nav span{padding:0 14px;border-left:1px solid #aab}
.foot-nav span:first-child{padding-left:0;border-left:none}
.foot-brand{left:655px;top:1094px;width:210px;text-align:center;color:#fff}
.foot-brand b{font-family:"Oxygen",sans-serif;font-weight:700;font-size:22px;display:block;margin-bottom:12px}
.foot-brand small{font-family:"Oxygen",sans-serif;font-weight:700;font-size:9.5px;line-height:13px;display:block;white-space:nowrap}
</style>
</head>
<body>

<header class="abs site-header"></header>
<div class="abs brand">
  <span class="brand-name">VERMILION</span>
  <span class="brand-sub">REEL WORKS</span>
</div>
<div class="abs call">
  <svg width="26" height="26" viewBox="0 0 26 26"><circle cx="13" cy="13" r="12" fill="none" stroke="#555" stroke-width="1.5"/><path d="M9 7c-2 2 0 8 4 11 2 1 3 1 4 0l-2-3-2 1c-1-1-3-4-3-6l2-1-1-3z" fill="#555"/></svg>
  <div><div class="call-label">Call Us Today</div><div class="call-number">86 21&nbsp; 5550-0148</div></div>
</div>
<div class="abs lang">LANGUAGE
  <svg width="14" height="9" viewBox="0 0 14 9"><path d="M0 0h14L7 9z" fill="var(--navy)"/></svg>
</div>
<nav class="abs nav">
  <a>HOME</a><a>ABOUT US</a><a>TEAM</a><a>SERVICES</a><a>FACILITY</a><a>CONTACT US</a><a>JOB OPPORTUNITIES</a>
</nav>

<div class="abs hero" role="img" aria-label="Sound engineer working at a mixing console with monitors in a warm-lit studio"></div>
<div class="abs hero-arrow" style="left:119px"><svg width="29" height="29"><path d="M17 8l-6 6.5 6 6.5" stroke="#fff" stroke-width="1.5" fill="none"/></svg></div>
<div class="abs hero-arrow" style="left:827px"><svg width="29" height="29"><path d="M12 8l6 6.5-6 6.5" stroke="#fff" stroke-width="1.5" fill="none"/></svg></div>
<div class="abs hero-caption">Vermilion Reel Works provides a well-designed working environment which amplifies<br>your team’s ability to reach their creative goals</div>

<h2 class="abs section-title" style="top:479px">
  <svg class="title-rule" width="200" height="14" viewBox="0 0 200 14"><g fill="#333"><path d="M0 2.5L194 1.5l6 2.5L0 3.5z"/><path d="M60 6H196l3 2.2H60z"/><path d="M110 10.5H194l3 2.2H110z"/></g></svg>
  <span>ABOUT VERMILION REEL WORKS</span>
  <svg class="title-rule right" width="200" height="14" viewBox="0 0 200 14"><g fill="#333"><path d="M0 2.5L194 1.5l6 2.5L0 3.5z"/><path d="M60 6H196l3 2.2H60z"/><path d="M110 10.5H194l3 2.2H110z"/></g></svg>
</h2>
<div class="abs about-text">
  <p>We are located in the premiere South-Bund area of Shanghai. Occupying a 5000 square meter Technical Building, Vermilion Reel Works was built by a filmmaker for filmmakers, and is one of the largest, most versatile full-service post-production facilities in China</p>
  <p>Vermilion Reel Works is positioning to be at the forefront of the latest technology. Our goal is to provide a comprehensive solution for<br>the post-production needs of our clients.</p>
</div>
<div class="abs read-more">READ MORE &gt;&gt;</div>

<section class="abs services"></section>
<h2 class="abs section-title" style="top:624px">
  <svg class="title-rule" width="205" height="14" viewBox="0 0 205 14"><g fill="#333"><path d="M0 2.5L199 1.5l6 2.5L0 3.5z"/><path d="M45 6H201l3 2.2H45z"/><path d="M100 10.5H199l3 2.2H100z"/></g></svg>
  <span>OUR SERVICES</span>
  <svg class="title-rule right" width="205" height="14" viewBox="0 0 205 14"><g fill="#333"><path d="M0 2.5L199 1.5l6 2.5L0 3.5z"/><path d="M45 6H201l3 2.2H45z"/><path d="M100 10.5H199l3 2.2H100z"/></g></svg>
</h2>
<div class="abs svc-arrow" style="left:80px"><svg width="28" height="28"><path d="M16 9l-5 5 5 5" stroke="#fff" stroke-width="2" fill="none"/></svg></div>
<div class="abs svc-arrow" style="left:876px"><svg width="28" height="28"><path d="M12 9l5 5-5 5" stroke="#fff" stroke-width="2" fill="none"/></svg></div>

<div class="abs service" style="left:116px"><div class="service-disc">
  <svg width="42" height="42" viewBox="0 0 42 42" fill="var(--navy)"><circle cx="15" cy="12" r="6"/><circle cx="28" cy="12" r="6"/><rect x="10" y="17" width="22" height="11" rx="2"/><path d="M32 20l7-3v11l-7-3z"/><path d="M3 20h7v5H3z"/><path d="M21 28l-7 11M21 28l7 11" stroke="var(--navy)" stroke-width="2.5"/></svg>
</div><div class="service-label">FEATURE FILMS</div></div>
<div class="abs service" style="left:268px"><div class="service-disc">
  <svg width="44" height="44" viewBox="0 0 44 44"><circle cx="20" cy="20" r="17" fill="var(--navy)"/><circle cx="20" cy="20" r="7" fill="none" stroke="#ddd" stroke-width="2"/><circle cx="20" cy="20" r="3" fill="#ddd"/><path d="M31 16v20" stroke="var(--navy)" stroke-width="3"/><circle cx="28" cy="37" r="5" fill="var(--navy)"/><path d="M31 16l7 4" stroke="var(--navy)" stroke-width="3"/></svg>
</div><div class="service-label">MUSIC &amp; SCORING</div></div>
<div class="abs service" style="left:417px"><div class="service-disc">
  <svg width="42" height="40" viewBox="0 0 42 40"><path d="M14 2l7 8 7-8" stroke="var(--navy)" stroke-width="2.5" fill="none"/><rect x="2" y="10" width="38" height="27" rx="4" fill="var(--navy)"/><rect x="7" y="15" width="22" height="17" rx="3" fill="#ddd"/><circle cx="34" cy="19" r="2" fill="#ddd"/><circle cx="34" cy="27" r="2" fill="#ddd"/></svg>
</div><div class="service-label">COMMERCIALS</div></div>
<div class="abs service" style="left:566px"><div class="service-disc">
  <svg width="46" height="40" viewBox="0 0 46 40"><path d="M24 3c-2 3 2 5-1 10" stroke="var(--navy)" stroke-width="2.5" fill="none"/><path d="M6 14h34c5 0 6 22 1 23-4 1-7-6-10-6H15c-3 0-6 7-10 6-5-1-4-23 1-23z" fill="var(--navy)"/><path d="M10 22h8M14 18v8" stroke="#ddd" stroke-width="2.5"/><circle cx="31" cy="20" r="2" fill="#ddd"/><circle cx="35" cy="24" r="2" fill="#ddd"/></svg>
</div><div class="service-label">VIDEO GAME</div></div>
<div class="abs service" style="left:723px"><div class="service-disc">
  <svg width="54" height="40" viewBox="0 0 54 40" fill="var(--navy)"><rect x="2" y="14" width="8" height="12"/><path d="M10 14l22-12v36L10 26z"/><ellipse cx="32" cy="20" rx="6" ry="18"/><path d="M41 10c3 6 3 14 0 20M46 6c4 9 4 19 0 28M51 3c5 11 5 23 0 34" stroke="var(--navy)" stroke-width="2" fill="none"/></svg>
</div><div class="service-label">SOUND DESIGN</div></div>

<!-- facilities -->
<div class="abs" style="left:115px;top:850px;width:229px">
  <div class="col-title"><svg width="30" height="22" viewBox="0 0 30 22"><path d="M4 16V12a11 11 0 0 1 22 0v4" stroke="#555" stroke-width="2.5" fill="none"/><rect x="2" y="12" width="6" height="9" rx="2" fill="#555"/><rect x="22" y="12" width="6" height="9" rx="2" fill="#555"/></svg><span><em>OUR</em> FACILITIES</span></div>
  <ul class="facility-list" style="margin-top:6px">
    <li>Executive business services with office assistance</li>
    <li>Unlimited worldwide calling</li>
    <li>Hi-speed internet and wireless network</li>
    <li>On-site massage therapy</li>
    <li>Entertainment and workout area</li>
    <li>Coffee bar and wine lounge</li>
  </ul>
  <div class="link-more" style="text-align:right;margin-top:7px;padding-right:9px">Read more »</div>
</div>

<!-- testimonials -->
<div class="abs" style="left:372px;top:850px;width:229px">
  <div class="col-title"><svg width="22" height="20" viewBox="0 0 22 20" fill="#555"><path d="M1 1h13v9H6l-4 4v-4H1z"/><path d="M16 5h5v10h-1v4l-4-4H8v-3h8z"/></svg><span><em>CLIENT</em> TESTIMONIALS</span></div>
</div>
<div class="abs quote"><svg width="16" height="14" style="float:left;margin:2px 5px 0 0" viewBox="0 0 16 14" fill="#c9c9c9"><path d="M0 14V7l4-7h3L5 6h2v8zM9 14V7l4-7h3l-2 6h2v8z"/></svg>Duis autem vel eum iriureol hder in vultat velit esse moles congat vela ilu dolor feugiat.Duis autem vel eum ure hendrern vultat velit esse autm vel eum iriure dol</div>
<svg class="abs" style="left:560px;top:1000px" width="30" height="16"><path d="M0 0h30L4 16z" fill="#ebebeb"/></svg>
<div class="abs avatar" role="img" aria-label="Client portrait photo"></div>
<div class="abs" style="left:457px;top:1011px;font-size:10px;color:#222">Mr. Lorem ispum</div>
<div class="abs link-more" style="left:530px;top:1025px">Read more »</div>

<!-- quick contact -->
<div class="abs" style="left:630px;top:850px;width:230px">
  <div class="col-title"><svg width="20" height="20" viewBox="0 0 20 20"><path d="M2 2h10M2 2v16h14v-6" stroke="#555" stroke-width="2" fill="none"/><path d="M8 13l1-4 8-8 3 3-8 8z" fill="#555"/></svg><span><em>QUICK</em> CONTACT</span></div>
</div>
<div class="abs field" style="top:895px">Name</div>
<div class="abs field" style="top:924px">Email</div>
<div class="abs field" style="top:953px;height:58px">Message</div>
<div class="abs submit">Submit</div>

<!-- footer -->
<footer class="abs site-footer"></footer>
<div class="abs foot-box" style="left:114px;width:200px">
  <h4>Subscribe to Newsletter</h4>
  <div style="display:flex"><div class="email-input">Email here</div><div class="go"><svg width="10" height="12"><path d="M2 1l5 5-5 5" stroke="#fff" stroke-width="2.5" fill="none"/></svg></div></div>
</div>
<div class="abs foot-box" style="left:353px;width:154px">
  <h4 style="margin-bottom:3px">Contact Us</h4>
  <div class="foot-contact"><svg width="12" height="11" viewBox="0 0 12 11"><path d="M2 1c-2 2 1 7 5 9l2-1-1-3-2 1c-1-1-2-2-2-4l1-1z" fill="#fff"/></svg>86 21 5550-0148</div>
  <div class="foot-contact"><svg width="12" height="9" viewBox="0 0 12 9"><rect x=".5" y=".5" width="11" height="8" fill="none" stroke="#fff"/><path d="M.5 .5l5.5 5 5.5-5" stroke="#fff" fill="none"/></svg>hello@vermilionreel.example</div>
</div>
<div class="abs foot-box" style="left:547px;width:96px">
  <h4>Follow Us</h4>
  <div style="display:flex;gap:12px;margin-top:12px"><div class="social" style="background:#4f6fb3"></div><div class="social" style="background:#46b9e3"></div><div class="social" style="background:#ef8a22"></div></div>
</div>
<div class="abs foot-brand">
  <b>VERMILION</b>
  <small>Copyright 2014 Vermilion Reel Works</small>
  <small>All Rights Reserved</small>
</div>
<div class="abs foot-nav"><span>Home</span><span>About Us</span><span>Team</span><span>Services</span><span>Facility</span><span>Contact Us</span><span>Job Opportunities</span></div>

</body>
</html>
```